Design Startseite Kanzlei-Homepage
Zielgruppe
Wir sind eine Rechtsanwaltskanzlei in Kempten (Allgäu) und regional sowie überregional in verschiedenen Rechtsgebieten tätig. Unsere Zielgruppe sind sowohl private als auch gewerbliche Mandanten.
Aufgabenstellung
Die bestehende Gestaltung wirkt derzeit aus unserer Sicht überholt. Insbesondere soll das bislang dominierende Rot vollständig entfallen.
Stattdessen stellen wir uns ein modernes, hochwertiges Erscheinungsbild vor, primär in dunklen Farbtönen (Anthrazit/Schwarz) kombiniert mit Beige- bzw. warmen Naturtönen. Ziel ist eine klare visuelle Anlehnung an unsere Kanzleiräumlichkeiten (siehe Fotos).
Die Webseite soll insgesamt moderner, klarer und visuell anspruchsvoller wirken, ohne an Seriosität und Zugänglichkeit einzubüßen. Die Balance zwischen hochwertigem Erscheinungsbild und mandantenorientierter Nutzerführung steht für uns im Vordergrund.

```html
<!DOCTYPE html>
<html lang="de">
<head>
<meta charset="utf-8">
<title>Kanzlei am Markt – Startseite</title>
<link href="https://fonts.googleapis.com/css2?family=Manrope:wght@300;400;500;600;700;800&family=Space+Mono:wght@400;700&display=swap" rel="stylesheet">
<style>
:root{
  --canvas:#ffffff;
  --hero:#181614;
  --ink:#121110;
  --band:#151312;
  --foot:#141211;
  --white:#f2efea;
  --text:#bdb7ae;
  --muted:#6f6860;
  --dim:#3a3531;
  --ghost:#2a2623;
  --deco:#5b4e43;
  --beige:#f0cfa3;
  --line:#2a2724;
  --photo-a:#d9d9d9;
  --photo-b:#2b2b2b;
}
*{margin:0;padding:0;box-sizing:border-box}
html,body{width:1200px;height:1200px;overflow:hidden;background:var(--canvas)}
body{font-family:"Manrope",sans-serif;color:var(--white)}
.page{position:absolute;left:425px;top:11px;width:560px;height:1895px;transform:scale(.625);transform-origin:0 0;overflow:hidden;background:var(--ink)}
.abs{position:absolute}
.mono{font-family:"Space Mono",monospace;letter-spacing:.12em;text-transform:uppercase}
.grid{background-image:linear-gradient(rgba(255,255,255,.025) 1px,transparent 1px),linear-gradient(90deg,rgba(255,255,255,.025) 1px,transparent 1px);background-size:28px 28px}

/* brand */
.brand{display:flex;align-items:center;gap:5px;font-weight:600;font-size:8px;letter-spacing:.02em;color:var(--white);white-space:nowrap}
.brand-mark{width:6px;height:6px;background:var(--beige)}

/* hero */
.hero{left:0;top:0;width:560px;height:448px;background-color:var(--hero);overflow:hidden}
.nav{right:35px;top:13px;display:flex;gap:22px;font-size:6.5px;color:var(--text)}
.nav .active{color:var(--beige)}
.deco-word{font-weight:500;color:var(--deco);line-height:1;letter-spacing:-.02em;white-space:nowrap}
.photo{background:linear-gradient(135deg,var(--photo-a),#8a8a8a 45%,var(--photo-b))}
.eyebrow{display:flex;align-items:center;gap:8px;font-size:6.5px;color:var(--beige)}
.eyebrow::before{content:"";width:22px;height:1px;background:var(--beige)}
.hero-title{font-weight:700;font-size:50px;line-height:1;letter-spacing:-.03em}
.hero-sub{font-weight:500;font-size:50px;line-height:1;letter-spacing:-.03em;color:#4a4540}
.lead{font-size:8px;line-height:1.55;color:var(--text);width:175px}
.btn-solid{background:var(--beige);color:#3a2c1e;font-size:6.5px;display:flex;align-items:center;justify-content:center}
.phone{font-size:7px;color:var(--white)}

/* philosophy */
.philo{left:0;top:448px;width:560px;height:375px;background:var(--ink)}
.label-dim{font-size:6px;color:var(--dim)}
.h2{font-weight:600;font-size:22px;line-height:1.25;letter-spacing:-.02em}
.h2 em{font-style:italic;font-weight:300;color:var(--beige);margin-right:4px}
.copy{font-size:7.3px;line-height:1.75;color:var(--text);width:254px}
.quote{border-left:1px solid var(--muted);padding-left:11px;width:254px}

/* expertise */
.expertise{left:0;top:823px;width:560px;height:867px;background:var(--band)}
.ghost-word{font-weight:700;font-size:96px;color:var(--ghost);letter-spacing:-.02em;line-height:1}
.areas{left:42px;top:218px;width:476px;list-style:none;border-top:1px solid var(--line)}
.area{height:67px;border-bottom:1px solid var(--line);display:flex;align-items:center;position:relative}
.area-no{position:absolute;left:10px;font-size:5.5px;color:var(--dim)}
.area-name{position:absolute;left:33px;font-size:16px;font-weight:400;color:var(--white)}
.area-desc{position:absolute;left:186px;width:216px;font-size:6.8px;line-height:1.6;color:var(--text)}
.cta-title{left:0;width:560px;top:710px;text-align:center;font-size:25px;font-weight:400;line-height:1.1;letter-spacing:-.02em}
.cta-title em{font-style:italic;font-weight:300;color:var(--beige);margin-right:4px}
.btn-outline{left:211px;top:780px;width:138px;height:29px;border:1px solid var(--beige);color:var(--beige);font-size:6.5px;display:flex;align-items:center;justify-content:center}

/* footer */
.footer{left:0;top:1690px;width:560px;height:205px;background-color:var(--foot)}
.foot-name{font-size:5.5px;font-weight:800;letter-spacing:.04em}
.foot-text{font-size:5.5px;line-height:2.1;color:var(--text)}
.foot-head{font-size:4.5px;color:var(--dim)}
.legal{font-size:4.5px;color:var(--dim)}
</style>
</head>
<body>
<div class="page">

  <section class="abs hero grid">
    <div class="abs brand" style="left:35px;top:13px"><span class="brand-mark"></span>Kanzlei am Markt</div>
    <nav class="abs nav mono">
      <span>Rechtsgebiete</span><span class="active">Kanzlei</span><span>Aktuelles</span><span>Kontakt</span>
    </nav>
    <div class="abs deco-word" style="left:276px;top:30px;font-size:92px">JURIS</div>
    <div class="abs photo" role="img" aria-label="Foto: Empfangsbereich der Kanzlei mit beleuchtetem Tresen" style="left:326px;top:78px;width:234px;height:336px"></div>
    <div class="abs deco-word" style="left:-14px;top:278px;font-size:80px;opacity:.85">PRUDEN</div>
    <div class="abs photo" role="img" aria-label="Foto: Flur mit Empfangstresen" style="left:291px;top:310px;width:121px;height:137px;background:linear-gradient(160deg,#cfcfcf,#5a5a5a 55%,#1e1e1e)"></div>

    <div class="abs eyebrow mono" style="left:52px;top:170px">Kempten / Allgäu</div>
    <h1 class="abs" style="left:50px;top:198px">
      <span class="hero-title" style="display:block">Kanzlei</span>
      <span class="hero-sub" style="display:block">am Markt</span>
    </h1>
    <p class="abs lead" style="left:52px;top:314px">Kompetente Rechtsberatung und engagierte Vertretung. Ihre Experten für Familienrecht, Arbeitsrecht und Verkehrsrecht.</p>
    <a class="abs btn-solid mono" style="left:52px;top:370px;width:95px;height:26px">Erstgespräch →</a>
    <span class="abs phone mono" style="left:157px;top:379px">0831 555 210 40</span>
  </section>

  <section class="abs philo">
    <div class="abs photo" role="img" aria-label="Foto: Wartebereich mit Sitzbank und großem Bergbild" style="left:52px;top:76px;width:169px;height:223px;background:linear-gradient(160deg,#e0e0e0,#7a7a7a 45%,#1a1a1a)"></div>
    <div class="abs" style="left:234px;top:152px;width:1px;height:70px;background:var(--dim)"></div>
    <div class="abs label-dim mono" style="left:262px;top:56px">Philosophie &amp; Struktur</div>
    <h2 class="abs h2" style="left:262px;top:78px">Ihre individuellen<br><em>Interessen</em>im Zentrum.</h2>
    <p class="abs copy" style="left:262px;top:150px">Die Mitglieder unseres Anwaltsteams – jeweils ergänzt um ein ansprechend eingerichtetes und funktional ausgestattetes Sekretariat – spezialisieren sich in unterschiedliche Fachrichtungen, sodass für Sie eine große Bandbreite in der mandantenorientierten Rechtsberatung sichergestellt ist.</p>
    <p class="abs copy quote" style="left:262px;top:228px">Auf die Mandatierung externer Anwälte kann durch die thematische Vielfalt und Spezialisierung unserer Juristen in den meisten Fällen verzichtet werden.</p>
    <p class="abs copy" style="left:262px;top:280px">Gleichzeitig gewährleistet unser engagiertes Kanzleiteam eine rechtliche Unterstützung ganz nach Ihren individuellen Interessen, stets auf dem neuesten Stand von Rechtsprechung und Praxis.</p>
  </section>

  <section class="abs expertise">
    <div class="abs ghost-word" style="left:32px;top:78px">EXPERTISE</div>
    <div class="abs eyebrow mono" style="left:52px;top:110px">Rechtsgebiete</div>
    <h2 class="abs h2" style="left:52px;top:127px;font-weight:500">Spezialisierte<br>Fokusbereiche.</h2>
    <ul class="abs areas">
      <li class="area"><span class="area-no mono">01</span><span class="area-name">Familienrecht</span><span class="area-desc">Streitigkeiten zwischen Ehe- und Lebenspartnern verlaufen nicht selten langwierig. Wir beraten bei sämtlichen Fragestellungen rund um Ehe, Scheidung und Unterhalt.</span></li>
      <li class="area"><span class="area-no mono">02</span><span class="area-name">Arbeitsrecht</span><span class="area-desc">Wir fungieren für Arbeitnehmer und Arbeitgeber als Ansprechpartner beim Abschluss und der Auflösung von Arbeitsverträgen, beraten bei Kündigungen.</span></li>
      <li class="area"><span class="area-no mono">03</span><span class="area-name">Verkehrsrecht</span><span class="area-desc">Wir unterstützen Sie dabei, Ihr Schmerzensgeld oder Entschädigungszahlungen nach Unfällen durchzusetzen und Ordnungswidrigkeitsverfahren abzuwenden.</span></li>
      <li class="area"><span class="area-no mono">04</span><span class="area-name">Strafrecht</span><span class="area-desc">Kompetente Rechtsberatung, die für Sie ein faires Verfahren sowie die Einhaltung Ihrer prozessualen Rechte während Durchsuchung und Vernehmung sicherstellt.</span></li>
      <li class="area"><span class="area-no mono">05</span><span class="area-name">Erbrecht</span><span class="area-desc">Wir beraten und vertreten Erben und Erblasser vor und nach dem Erbfall in allen rechtlichen Fragen für eine rechtlich fundierte Betrachtung.</span></li>
      <li class="area"><span class="area-no mono">06</span><span class="area-name">Mietrecht</span><span class="area-desc">Ob zu Mietverträgen, Mieterhöhungen oder Räumungen: Wir vertreten Vermieter und Mieter in Kempten und dem Allgäu fachkundig.</span></li>
    </ul>
    <h2 class="abs cta-title">Bereit für ein<br><em>persönliches</em>Gespräch?</h2>
    <a class="abs btn-outline mono">Termin vereinbaren →</a>
  </section>

  <footer class="abs footer grid">
    <div class="abs brand" style="left:52px;top:38px"><span class="brand-mark"></span>Kanzlei am Markt</div>
    <div class="abs foot-name" style="left:52px;top:66px">KANZLEI AM MARKT</div>
    <div class="abs foot-text" style="left:52px;top:78px">Lindenweg 7<br>87435 Kempten</div>
    <div class="abs foot-text" style="left:52px;top:112px">T. 0831 · 555 210 40</div>
    <div class="abs foot-text" style="left:52px;top:128px">M. info@kanzlei-am-markt.de</div>
    <div class="abs foot-head mono" style="left:290px;top:38px">Rechtliches</div>
    <div class="abs foot-text" style="left:290px;top:52px;color:var(--white)">Impressum<br>Datenschutz<br>Sitemap</div>
    <div class="abs foot-head mono" style="left:409px;top:38px">Informationen</div>
    <div class="abs foot-text" style="left:409px;top:52px;color:var(--white)">Anfahrt<br>Routenplaner</div>
    <div class="abs legal mono" style="left:52px;top:180px">© 2026 Kanzlei am Markt. Alle Rechte vorbehalten.</div>
  </footer>

</div>
</body>
</html>
```